Social media design templates

A variety of templates incorporating our logo and colours to use for our postings on different social media platforms. Must be user friendly and meet our brand image. We have attached our logo to view. We would like some of the templates to offer the ability to insert a background image and others to be a template designed around our logo.

We are black and white in colour, and our values speak to our transparency and honesty, so we are looking for clean cut, sharp straight lines, not using any other colours or curved lines.

We are a recruitment company that will be using these templates
- job posting,
- general announcements,
- blog,
- company newsletter,
- updates,
- testimonials and
- top candidate profiles

We would like a gallery of templates to choose from to use separately that all represent our brand.

```html
<!DOCTYPE html>
<html lang="en">
<head>
<meta charset="utf-8">
<title>Northline Group – Social Templates</title>
<link href="https://fonts.googleapis.com/css2?family=Outfit:wght@400;700;800&display=swap" rel="stylesheet">
<style>
  :root {
    --bg: #b9b9bb;
    --black: #000000;
    --white: #ffffff;
    --ink: #111111;
    --photo-dusk-a: #5b5660;
    --photo-dusk-b: #7a6a74;
    --photo-dusk-c: #4a4650;
    --photo-glow-a: #f4eef2;
    --photo-glow-b: #c98aa0;
    --photo-glow-c: #4d5b7a;
    --photo-desk-a: #5c5c5e;
    --photo-desk-b: #3f3f41;
  }
  * { margin: 0; padding: 0; box-sizing: border-box; }
  html, body { width: 1200px; height: 435px; overflow: hidden; }
  body {
    background: var(--bg);
    font-family: "Outfit", sans-serif;
    position: relative;
  }
  .template {
    position: absolute;
    top: 30px;
    width: 359px;
    height: 360px;
    overflow: hidden;
    box-shadow: 0 2px 6px rgba(0,0,0,0.25);
  }
  .template--job { left: 31px; background: var(--white); }
  .template--title-blocks { left: 420px; background: var(--white); }
  .template--title-photo { left: 809px; background: var(--photo-desk-a); }

  .photo { position: absolute; }
  .photo--skyline {
    left: 206px; top: 0; width: 153px; height: 360px;
    background: linear-gradient(180deg, var(--photo-dusk-a) 0%, var(--photo-dusk-b) 45%, var(--photo-dusk-c) 100%);
  }
  .photo--team {
    left: 0; top: 0; width: 359px; height: 184px;
    background: linear-gradient(90deg, var(--photo-glow-c) 0%, var(--photo-glow-b) 30%, var(--photo-glow-a) 50%, var(--photo-glow-b) 72%, var(--photo-glow-c) 100%);
  }
  .photo--handshake {
    left: 0; top: 0; width: 359px; height: 360px;
    background: linear-gradient(135deg, var(--photo-desk-a) 0%, #6a6a6c 50%, var(--photo-desk-b) 100%);
  }

  .brand-block {
    position: absolute;
    background: var(--black);
    color: var(--white);
    display: flex;
    flex-direction: column;
    align-items: center;
    justify-content: center;
    gap: 6px;
  }
  .brand-block .brand-square { width: 26px; height: 26px; border: 1.5px solid var(--white); }
  .brand-name {
    font-weight: 700;
    font-size: 8.5px;
    letter-spacing: 0.8px;
    text-align: center;
    line-height: 1.3;
  }
  .brand-block--job { left: 23px; top: 0; width: 81px; height: 87px; }
  .brand-block--corner { left: 258px; top: 255px; width: 82px; height: 105px; justify-content: flex-start; padding-top: 10px; }

  .brand-inline {
    position: absolute; right: 20px; top: 20px;
    display: flex; align-items: center; gap: 7px;
    color: var(--white);
  }
  .brand-inline .brand-square { width: 37px; height: 37px; border: 1.5px solid var(--white); }
  .brand-inline .brand-name { font-size: 10px; text-align: left; }

  .headline {
    font-weight: 800;
    letter-spacing: -0.5px;
  }
  .template--job .headline {
    position: absolute; left: 22px; top: 97px;
    font-size: 35px; line-height: 34px; color: var(--ink);
  }
  .subline { font-weight: 400; }
  .template--job .subline {
    position: absolute; left: 23px; top: 168px;
    font-size: 12.5px; color: var(--ink);
  }
  .body-copy {
    position: absolute; left: 23px; top: 246px; width: 168px;
    font-size: 6.8px; line-height: 9.2px; color: var(--ink);
    text-align: justify;
  }
  .contact-list {
    position: absolute; left: 27px; top: 300px;
    list-style: none; font-size: 5px; color: var(--ink);
  }
  .contact-list li { display: flex; align-items: center; gap: 13px; height: 15.5px; }
  .contact-list svg { width: 8px; height: 8px; }

  .title-bars { position: absolute; left: 21px; top: 207px; }
  .title-bar {
    display: block;
    width: max-content;
    background: var(--black);
    color: var(--white);
    font-weight: 800;
    font-size: 34px;
    line-height: 40px;
    padding: 0 7px;
    letter-spacing: -0.5px;
  }
  .title-bar + .title-bar { margin-top: 7px; }
  .template--title-blocks .subline {
    position: absolute; left: 21px; top: 297px;
    font-size: 16.5px; color: var(--ink);
  }
  .website {
    position: absolute; font-size: 7px; letter-spacing: 0.2px;
  }
  .template--title-blocks .website { left: 24px; top: 332px; color: var(--ink); }

  .template--title-photo .headline {
    position: absolute; left: 35px; top: 175px;
    font-size: 50px; line-height: 47px; letter-spacing: -1px; color: var(--white);
  }
  .template--title-photo .subline {
    position: absolute; left: 35px; top: 274px;
    font-size: 16.5px; color: var(--white);
  }
  .template--title-photo .website { left: 0; width: 359px; text-align: center; top: 336px; color: var(--white); }
</style>
</head>
<body>

  <section class="template template--job">
    <div class="photo photo--skyline" role="img" aria-label="Silhouettes of two business people blended with a city skyline at dusk"></div>
    <div class="brand-block brand-block--job">
      <span class="brand-square"></span>
      <span class="brand-name">NORTHLINE<br>GROUP</span>
    </div>
    <h1 class="headline">JOB<br>POSTING</h1>
    <p class="subline">Lorem ipsum dolor sit amet,</p>
    <p class="body-copy">Lorem ipsum dolor sit amet, consectetuer adipiscing elit, sed diam nonummy nibh euismod tincidunt ut laoreet dolore magna aliquam erat volutpat. Ut wisi enim ad minim veniam</p>
    <ul class="contact-list">
      <li>
        <svg viewBox="0 0 10 10"><path d="M5 0.5a3.2 3.2 0 0 0-3.2 3.2C1.8 6 5 9.5 5 9.5S8.2 6 8.2 3.7A3.2 3.2 0 0 0 5 0.5zm0 4.5a1.3 1.3 0 1 1 0-2.6 1.3 1.3 0 0 1 0 2.6z" fill="#111"/></svg>
        Your location here
      </li>
      <li>
        <svg viewBox="0 0 10 10"><rect x="0.8" y="2" width="8.4" height="6" fill="none" stroke="#111" stroke-width="1"/><path d="M0.8 2L5 5.4 9.2 2" fill="none" stroke="#111" stroke-width="1"/></svg>
        your@emailhere.com
      </li>
      <li>
        <svg viewBox="0 0 10 10"><path d="M2.2 0.8l1.6 2-0.9 1.2c0.6 1.2 1.5 2.1 2.7 2.7l1.2-0.9 2 1.6-0.9 1.6C4.7 9 1 5.3 0.8 1.7z" fill="#111"/></svg>
        012-456789
      </li>
    </ul>
  </section>

  <section class="template template--title-blocks">
    <div class="photo photo--team" role="img" aria-label="Silhouettes of a business team shaking hands, blended with a city skyline and bright sky"></div>
    <h1 class="title-bars">
      <span class="title-bar">YOUR</span>
      <span class="title-bar">TITLE HERE</span>
    </h1>
    <p class="subline">Lorem ipsum dolor sit amet,</p>
    <p class="website">www.yourwebsitehere.com</p>
    <div class="brand-block brand-block--corner">
      <span class="brand-square"></span>
      <span class="brand-name">NORTHLINE<br>GROUP</span>
    </div>
  </section>

  <section class="template template--title-photo">
    <div class="photo photo--handshake" role="img" aria-label="Dimmed photo of two business people shaking hands over a signed contract"></div>
    <div class="brand-inline">
      <span class="brand-square"></span>
      <span class="brand-name">NORTHLINE<br>GROUP</span>
    </div>
    <h1 class="headline">YOUR<br>TITLE HERE</h1>
    <p class="subline">Lorem ipsum dolor sit amet,</p>
    <p class="website">www.yourwebsitehere.com</p>
  </section>

</body>
</html>
```